Brisk Harbour Finance Business Cards

Looking for a business card for a new mortgage broking business. Name of the business is Brisk Harbour Finance. Purpose of the business is to build trust and strong relationships with clients to then assist them with your mortgage lending needs. Most relationships within the business start off as an enquiry, and then can evolve into a 10+ year relationship, servicing clients from purchasing a new home to then upgrading for their family and even then assisting their children with their first home purchase. Business card should communicate financial security and trust.

Target Market(s)

Targeting professional clients who are looking to build a relationship with a knowledgeable mortgage professional

Industry/Entity Type

Finance - Home Loans

Contact Information for Business Card

Peter Holcroft, Director, mobile: 0471 926058, email:peter@briskharbourfinance.com.au, website: www.briskharbourfinance.com.au

Font styles to use
Sans Serif

Requirements
Must have
• On the front: Must have company logo, contact details as above. On the back: slogan, 'full of choices, free of stress', plus listing services offered: home loans, investment loans, first home buyers, refinancing, car finance

```html
<!DOCTYPE html>
<html lang="en">
<head>
<meta charset="utf-8">
<title>Brisk Harbour Finance Business Cards</title>
<link rel="stylesheet" href="https://fonts.googleapis.com/css2?family=Arimo:wght@400;700&family=Roboto+Condensed:wght@400;700&display=swap">
<style>
  :root {
    --navy: #0b4f7c;
    --navy-deep: #064470;
    --navy-light: #0d6496;
    --orange: #f5a000;
    --white: #ffffff;
    --rule: #9a9a9a;
    --stage: #2a2a2a;
  }
  * { box-sizing: border-box; margin: 0; padding: 0; }
  html, body { width: 1200px; height: 1108px; overflow: hidden; }
  body {
    background: var(--stage);
    font-family: "Arimo", Arial, sans-serif;
    position: relative;
  }
  .card {
    position: absolute;
    top: 169px;
    width: 440px;
    height: 770px;
    border-radius: 22px;
    overflow: hidden;
  }
  .card-front { left: 130px; background: var(--white); color: var(--navy); }
  .card-back { left: 630px; background: var(--navy-deep); color: var(--white); }

  .brand {
    position: absolute;
    top: 130px; left: 0; right: 0;
    display: flex; align-items: center; justify-content: center; gap: 18px;
  }
  .brand-mark { width: 54px; height: 54px; border: 6px solid var(--navy); border-radius: 8px; }
  .brand-name {
    font-weight: 700; font-size: 34px; line-height: 1.05;
    color: var(--navy); text-transform: uppercase; letter-spacing: 0.5px;
  }

  .person { position: absolute; top: 462px; left: 0; right: 0; text-align: center; }
  .person-name { font-weight: 700; font-size: 30px; letter-spacing: 1px; text-transform: uppercase; color: var(--navy); }
  .person-role { font-size: 22px; color: var(--orange); margin-top: 2px; }

  .contact-icons {
    position: absolute; top: 548px; left: 40px; right: 40px;
    display: flex; align-items: center; gap: 8px;
  }
  .contact-icons .rule { flex: 1; height: 1px; background: var(--rule); }
  .icon {
    width: 40px; height: 40px; border-radius: 6px; background: var(--orange);
    display: flex; align-items: center; justify-content: center;
  }
  .icon svg { width: 26px; height: 26px; }

  .contact-lines {
    position: absolute; top: 612px; left: 0; right: 0;
    text-align: center; font-size: 21px; line-height: 1.45; color: var(--navy);
  }
  .contact-phone { font-size: 23px; }
  .accent { color: var(--orange); }

  .back-pattern { position: absolute; inset: 0;
    background: radial-gradient(ellipse at 70% 20%, var(--navy-light), var(--navy-deep) 70%); }

  .back-copy { position: absolute; top: 420px; left: 0; right: 0; text-align: center; }
  .slogan { font-weight: 700; font-size: 34px; line-height: 1.15; text-transform: uppercase; letter-spacing: 0.5px; }
  .slogan .line-one { color: var(--orange); }
  .slogan .line-two { color: var(--white); }
  .services-title {
    margin-top: 56px; font-weight: 700; font-size: 30px; color: var(--orange);
    text-transform: uppercase; letter-spacing: 0.5px;
  }
  .services-list {
    margin-top: 14px; list-style: none;
    font-family: "Roboto Condensed", "Arial Narrow", sans-serif;
    font-size: 25px; line-height: 1.35; color: var(--white);
  }
  .sep { color: var(--orange); padding: 0 6px; }
</style>
</head>
<body>

<section class="card card-front" aria-label="Business card front">
  <div class="brand">
    <span class="brand-mark"></span>
    <span class="brand-name">Brisk Harbour<br>Finance</span>
  </div>

  <div class="person">
    <p class="person-name">Peter Holcroft</p>
    <p class="person-role">Director</p>
  </div>

  <div class="contact-icons">
    <span class="rule"></span>
    <span class="icon" aria-label="Phone">
      <svg viewBox="0 0 24 24"><path fill="#fff" d="M6.6 10.8a15 15 0 0 0 6.6 6.6l2.2-2.2c.3-.3.7-.4 1-.2 1.1.4 2.3.6 3.6.6.6 0 1 .4 1 1V20c0 .6-.4 1-1 1A17 17 0 0 1 3 4c0-.6.4-1 1-1h3.5c.6 0 1 .4 1 1 0 1.3.2 2.5.6 3.6.1.3 0 .7-.2 1z"/></svg>
    </span>
    <span class="icon" aria-label="Email">
      <svg viewBox="0 0 24 24"><rect x="3" y="6" width="18" height="12" rx="1" fill="none" stroke="#fff" stroke-width="1.8"/><path d="M3 6l9 7 9-7" fill="none" stroke="#fff" stroke-width="1.8"/></svg>
    </span>
    <span class="icon" aria-label="Website">
      <svg viewBox="0 0 24 24"><circle cx="12" cy="12" r="9" fill="none" stroke="#fff" stroke-width="1.8"/><path d="M3 12h18M12 3c3 3 3 15 0 18M12 3c-3 3-3 15 0 18" fill="none" stroke="#fff" stroke-width="1.5"/></svg>
    </span>
    <span class="rule"></span>
  </div>

  <div class="contact-lines">
    <p class="contact-phone">0471 926058</p>
    <p>peter@briskharbourfinance.com.au</p>
    <p>www.<span class="accent">briskharbourfinance</span>.com.au</p>
  </div>
</section>

<section class="card card-back" aria-label="Business card back">
  <div class="back-pattern" role="img" aria-label="Repeating embossed brand pattern in blue tones"></div>
  <div class="back-copy">
    <p class="slogan"><span class="line-one">Full of choices</span><br><span class="line-two">Free of stress</span></p>
    <p class="services-title">Services Offered</p>
    <ul class="services-list">
      <li>Home Loans<span class="sep">|</span>Investment Loans</li>
      <li>First Home Buyers<span class="sep">|</span>Refinancing</li>
      <li>Car Finance</li>
    </ul>
  </div>
</section>

</body>
</html>
```